BrightKeel Business Card Contest

We are looking for a modern business card that catches attention and is unique. Attached is the brand guide and logo files. Please note that the back side (not the side with our name and info) with be UV raise printed, so have fun with the design there. We want to include Name, Title, Phone number, email, website.

Contact Information for Business Card

Please see project description

```html
<!DOCTYPE html>
<html lang="en">
<head>
<meta charset="utf-8">
<title>BrightKeel Business Card</title>
<link href="https://fonts.googleapis.com/css2?family=Figtree:wght@400;500;700&display=swap" rel="stylesheet">
<style>
  :root {
    --stage: #000000;
    --card: #ffffff;
    --ink: #1d1e26;
    --ink-soft: #3a3b44;
    --navy: #0b2f6b;
    --royal: #0c4fa0;
    --azure: #1f7fcf;
    --cyan: #1bc0e5;
    --mist: #91b8d1;
    --slate: #b2bbc9;
    --orange: #ef801e;
    --red: #da2e20;
  }
  * { box-sizing: border-box; margin: 0; padding: 0; }
  html, body { width: 1200px; height: 1200px; overflow: hidden; }
  body {
    background: var(--stage);
    font-family: "Figtree", sans-serif;
    color: var(--ink);
    position: relative;
  }
  .card {
    position: absolute;
    left: 237px;
    width: 729px;
    height: 416px;
    border-radius: 26px;
    overflow: hidden;
  }
  .card-front { top: 145px; background: var(--card); }
  .card-back {
    top: 627px;
    background:
      linear-gradient(160deg, transparent 0%, transparent 60%, rgba(145,184,209,0.9) 80%, rgba(145,184,209,1) 100%),
      linear-gradient(115deg, var(--red) 0%, var(--orange) 14%, var(--slate) 30%, var(--mist) 45%, var(--cyan) 60%, var(--cyan) 68%, var(--azure) 80%, var(--royal) 92%, var(--navy) 100%);
  }
  .brand {
    position: absolute;
    left: 45px;
    top: 52px;
    display: flex;
    align-items: center;
    gap: 12px;
  }
  .brand-square {
    width: 40px;
    height: 40px;
    background: var(--royal);
  }
  .brand-name {
    font-size: 46px;
    font-weight: 500;
    color: var(--ink);
    letter-spacing: -0.5px;
    line-height: 1;
  }
  .person {
    position: absolute;
    right: 49px;
    top: 208px;
    text-align: right;
  }
  .person-name {
    font-size: 29px;
    font-weight: 700;
    line-height: 1.1;
    letter-spacing: 0.2px;
  }
  .person-title {
    font-size: 20px;
    font-weight: 400;
    color: var(--ink-soft);
    margin-top: 2px;
  }
  .divider {
    position: absolute;
    left: 45px;
    right: 44px;
    top: 280px;
    height: 3px;
    border-radius: 2px;
    background: linear-gradient(90deg, var(--royal) 0%, var(--cyan) 20%, var(--mist) 40%, var(--orange) 65%, var(--red) 100%);
  }
  .contacts {
    position: absolute;
    left: 46px;
    top: 298px;
    list-style: none;
  }
  .contact-item {
    display: flex;
    align-items: center;
    gap: 14px;
    height: 26px;
    font-size: 20px;
    font-weight: 500;
  }
  .contact-icon { width: 18px; height: 18px; flex: none; }
</style>
</head>
<body>
  <section class="card card-front" aria-label="Business card front">
    <div class="brand">
      <span class="brand-square"></span>
      <span class="brand-name">BrightKeel</span>
    </div>
    <div class="person">
      <p class="person-name">MARCUS DELANE</p>
      <p class="person-title">Founder &amp; CEO</p>
    </div>
    <div class="divider"></div>
    <ul class="contacts">
      <li class="contact-item">
        <svg class="contact-icon" viewBox="0 0 24 24" fill="none" stroke="#1d1e26" stroke-width="1.8" stroke-linejoin="round"><path d="M5 3h4l2 5-2.5 1.5a11 11 0 0 0 6 6L16 13l5 2v4a2 2 0 0 1-2 2A16 16 0 0 1 3 5a2 2 0 0 1 2-2z"/><path d="M14 3a7 7 0 0 1 7 7M14 7a3 3 0 0 1 3 3"/></svg>
        <span>(123) 456-7890</span>
      </li>
      <li class="contact-item">
        <svg class="contact-icon" viewBox="0 0 24 24" fill="none" stroke="#1d1e26" stroke-width="1.4"><rect x="2" y="5" width="20" height="14"/><path d="M2 5l10 8 10-8"/></svg>
        <span>info@brightkeel.com</span>
      </li>
      <li class="contact-item">
        <svg class="contact-icon" viewBox="0 0 24 24" fill="none" stroke="#1d1e26" stroke-width="1.4"><circle cx="12" cy="12" r="10"/><ellipse cx="12" cy="12" rx="4.5" ry="10"/><path d="M2 12h20M4 7h16M4 17h16"/></svg>
        <span>brightkeel.com</span>
      </li>
    </ul>
  </section>

  <section class="card card-back" role="img" aria-label="Card back: angular rays of red, orange, grey-blue, cyan and deep blue fanning around a central brand emblem"></section>
</body>
</html>
```